Cover for a Series of 5 Poetry Books where there is only a subtle (colour?) change for each

I have 5 poetry books to publish all have the main title of Harbours Beneath Quiet Skies then have different subtitles, which are Drifting Alone Past Amber Straits; Drifting Alone Past Ember Bays, and 3 others I have yet to determine. I have already published the first one and will attach the cover, which needs re-doing for a reprint. I have been given permission to use a photograph of the moon and a universe star pic as I like the idea of using the moon, as it dominates the tides, oceans and weather systems. I like the thought of using the stars because I love to watch them out at sea and the first design of the book I really love, except that I don't have it in 30dpi which is a must. the photo of the boat on the front is a photo of my boat, and I would like to use it too if possible. all that said I am up for some new ideas that you come up with. my poetry is pretty raw at times, but can also be inspiring and I think the book cover needs to reflect this. I am a solo sailor so it has to reflect that too!
I would like the series of 5 books to have covers that are easily recognisable as a series but also are such that people want to pick them up and read. Maybe change the colour of the moon?
I will have a series of 5 books in paperback and e-books printed 6'x9' with approx 116 to 130 pages max I have the back cover info, the photo of the boat and photo of the author. I can get the barcode for the ISBN numbers. I am self-publishing so I do not have a heap of money!
I have had a couple of folk who have kindly reproduced what I already had, that is not what I am looking for. If I am still not clear, please do drop me a line. I am very new to this process.
Thanks
Target Market(s)
Male and female 15 to 35 and 65 to 85
Requirements
Must have
- 5 covers which are clearly slightly different, but recognisable as a series
Should not have
- unhelpful comments - thanks

```html
<!DOCTYPE html>
<html lang="en">
<head>
<meta charset="utf-8">
<title>Harbours Beneath Quiet Skies – Series Covers</title>
<link rel="stylesheet" href="https://fonts.googleapis.com/css2?family=Dancing+Script:wght@500;700&family=Kaushan+Script&display=swap">
<style>
  :root {
    --page-bg: #e9e4dc;
    --cover-shadow: rgba(40, 30, 20, 0.35);
    --ink-light: #ffffff;
    --title-amber: #f6a317;
    --ember-sky-top: #6b1f78;
    --ember-sky-mid: #8a2a6a;
    --ember-sea: #d8200f;
    --ember-moon: #ec5a22;
    --ember-moon-core: #f27a36;
    --amber-sky-top: #1b2f7a;
    --amber-sky-mid: #0e1740;
    --amber-sea: #1650a8;
    --amber-moon: #b9bde8;
    --amber-moon-core: #d8dbf4;
  }
  * { box-sizing: border-box; margin: 0; padding: 0; }
  html, body {
    width: 1200px;
    height: 789px;
    overflow: hidden;
    background: var(--page-bg);
  }
  .series {
    position: relative;
    width: 1200px;
    height: 789px;
    display: flex;
    justify-content: center;
    align-items: center;
    gap: 60px;
  }
  .cover {
    position: relative;
    width: 420px;
    height: 630px;
    overflow: hidden;
    box-shadow: 0 14px 30px var(--cover-shadow);
    color: var(--ink-light);
  }
  .cover__art {
    position: absolute;
    inset: 0;
  }
  .cover--ember .cover__art {
    background:
      radial-gradient(circle at 50% 58% , var(--ember-moon-core) 0, var(--ember-moon) 170px, rgba(236,90,34,0) 172px),
      linear-gradient(180deg, var(--ember-sky-top) 0%, var(--ember-sky-mid) 40%, #3a0f2a 62%, var(--ember-sea) 74%, #b0180c 100%);
  }
  .cover--amber .cover__art {
    background:
      radial-gradient(circle at 50% 59%, var(--amber-moon-core) 0, var(--amber-moon) 170px, rgba(185,189,232,0) 172px),
      linear-gradient(180deg, var(--amber-sky-top) 0%, var(--amber-sky-mid) 45%, #050a1c 70%, var(--amber-sea) 80%, #123c86 100%);
  }
  .cover__subtitle {
    position: absolute;
    top: 34px;
    right: 26px;
    font-family: "Dancing Script", cursive;
    font-weight: 700;
    font-size: 21px;
    letter-spacing: 0.2px;
  }
  .cover__title {
    position: absolute;
    top: 46px;
    left: 0;
    right: 0;
    text-align: center;
    font-family: "Dancing Script", cursive;
    font-weight: 700;
    line-height: 1;
  }
  .cover__title-main {
    display: block;
    font-size: 92px;
    text-shadow: 0 3px 6px rgba(0,0,0,0.45);
  }
  .cover__title-tail {
    display: block;
    margin: 2px 26px 0 0;
    text-align: right;
    font-size: 32px;
    font-weight: 500;
  }
  .cover--amber .cover__title-main { color: var(--title-amber); }
  .cover__author {
    position: absolute;
    bottom: 26px;
    left: 0;
    right: 0;
    text-align: center;
    font-family: "Kaushan Script", cursive;
    font-size: 40px;
  }
</style>
</head>
<body>
<main class="series">
  <article class="cover cover--ember">
    <div class="cover__art" role="img" aria-label="Photograph of a purple star-filled sky above a large orange-red full moon with a silhouetted sailboat on a red sea"></div>
    <p class="cover__subtitle">Drifting Alone Past Ember Bays</p>
    <h1 class="cover__title">
      <span class="cover__title-main">Harbours</span>
      <span class="cover__title-tail">Beneath Quiet Skies</span>
    </h1>
    <p class="cover__author">Author Name</p>
  </article>

  <article class="cover cover--amber">
    <div class="cover__art" role="img" aria-label="Photograph of a deep blue star-filled sky above a large pale full moon with a silhouetted sailboat on a calm blue sea"></div>
    <p class="cover__subtitle">Drifting Alone Past Amber Straits</p>
    <h1 class="cover__title">
      <span class="cover__title-main">Harbours</span>
      <span class="cover__title-tail">Beneath Quiet Skies</span>
    </h1>
    <p class="cover__author">Author Name</p>
  </article>
</main>
</body>
</html>
```